I am seeking a label design for a new product to be launched at my salon, T&M Salon. However, for the products, I am solely utilizing the branding "T&M."
I am interested in exploring various bathroom modern clean concepts for the labels on our shampoo and conditioner ROUND white 10 Oz bottles.
I need a shampoo label design that will attract many customers with its appeal. As the owner of a hair salon, I aim to create something unique and exquisite, with a clean and sleek, high-class, and elegant print for the shampoo. I am open to suggestions and eager to see different designs that may better suit my vision.

Also if you could apply the label on the bottle, would be amazing.

Target Market(s)

Anyone seeking healthy, smooth, fast-growing, and beautiful hair is our target market—primarily women, though we welcome all clients.

Industry/Entity Type

Hair and Spa.

Colors

Designer to choose colors to be used in the design.

Requirements
Must have
• Clean look, and no overcrowded with elements, No bright or solid dark colors .
Nice to have
• Please refer to the attached references below, but I am open to suggestions as well.

```html
<!DOCTYPE html>
<html lang="en">
<head>
<meta charset="UTF-8">
<title>T&amp;M Revitalizing Shampoo Label</title>
<link href="https://fonts.googleapis.com/css2?family=Bodoni+Moda:wght@400;500&family=Questrial&family=Cormorant+Garamond:wght@500&display=swap" rel="stylesheet">
<style>
  :root {
    --paper: #ffffff;
    --ink: #1d1d1d;
    --ink-soft: #3a3a3a;
    --rule: #444444;
  }
  * { box-sizing: border-box; margin: 0; padding: 0; }
  html, body {
    width: 1200px;
    height: 981px;
    overflow: hidden;
    background: var(--paper);
  }
  .label {
    position: relative;
    width: 1200px;
    height: 981px;
    color: var(--ink);
  }
  .brand-mark {
    position: absolute;
    left: 50%;
    top: 430px;
    width: 58px;
    height: 58px;
    margin-left: -29px;
    border: 1px solid var(--rule);
    border-radius: 50%;
    display: flex;
    align-items: center;
    justify-content: center;
  }
  .brand-name {
    font-family: "Bodoni Moda", serif;
    font-weight: 400;
    font-size: 20px;
    color: var(--ink);
    letter-spacing: 0.5px;
  }
  .variant {
    position: absolute;
    left: 0;
    right: 0;
    top: 531px;
    text-align: center;
    font-family: "Questrial", sans-serif;
    font-size: 17px;
    color: var(--ink-soft);
    letter-spacing: 0.3px;
  }
  .bracket {
    position: absolute;
    left: 50%;
    width: 174px;
    height: 48px;
    margin-left: -87px;
  }
  .bracket path {
    fill: none;
    stroke: var(--rule);
    stroke-width: 0.9;
  }
  .bracket-top { top: 545px; }
  .bracket-bottom { top: 697px; }
  .product-name {
    position: absolute;
    left: 0;
    right: 0;
    top: 600px;
    text-align: center;
    font-family: "Bodoni Moda", serif;
    font-weight: 500;
    font-size: 78px;
    line-height: 90px;
    letter-spacing: 1px;
    color: var(--ink);
    transform: scaleX(0.6);
  }
  .volume {
    position: absolute;
    left: 0;
    right: 0;
    top: 763px;
    text-align: center;
    font-family: "Cormorant Garamond", serif;
    font-weight: 500;
    font-size: 16px;
    letter-spacing: 0.5px;
    color: var(--ink);
  }
</style>
</head>
<body>
  <main class="label">
    <div class="brand-mark">
      <span class="brand-name">T&amp;M</span>
    </div>

    <p class="variant">Revitalizing</p>

    <svg class="bracket bracket-top" viewBox="0 0 174 48" aria-hidden="true">
      <path d="M1 1 C1 12 4 20 16 20 L70 20 C80 20 84 28 87 46 C90 28 94 20 104 20 L158 20 C170 20 173 12 173 1"/>
    </svg>

    <h1 class="product-name">SHAMPOO</h1>

    <svg class="bracket bracket-bottom" viewBox="0 0 174 48" aria-hidden="true">
      <path d="M1 47 C1 36 4 28 16 28 L70 28 C80 28 84 20 87 2 C90 20 94 28 104 28 L158 28 C170 28 173 36 173 47"/>
    </svg>

    <p class="volume">10 OZ</p>
  </main>
</body>
</html>
```